Expense Tracker App for Young Adults

I need a mobile app designer to design an app UI for me. It is for an expense tracker app. I’ve attached a mind map of the various screens and features of the app.

I would like to see designs for this app which is targeted towards young adults (late teens & early 20s) just starting their career who want to plan their budgets and track their expenses.
Updates

Hello designers! I'm conscious that this is not a guaranteed project, so I can understand that some of you might be apprehensive. Just wanted to let you know that I'm willing to see your initial drafts that show your direction and theme for design. You don't have to design the whole app. In fact, it's better if you share your initial design ideas so that we can have a discussion and I can give my input. If I see some good initial designs, I will be happy to make this a guaranteed project. I'm simply being cautious since I'm bootstrapping this and funding out of my own pocket. Thank you for your understanding!

Target Market(s)

Young adults who are just starting their careers, late teens and early 20s.

Font styles to use
Sans Serif

Requirements
Must have
• Ease of use, smart and sleek, a guided setup wizard which will help users setup their account after signing up.
Should not have
• Clunky

```html
<!DOCTYPE html>
<html lang="en">
<head>
<meta charset="UTF-8">
<title>Create an account</title>
<link href="https://fonts.googleapis.com/css2?family=Poppins:wght@400;500;600;700&display=swap" rel="stylesheet">
<style>
  :root {
    --bg: #ffffff;
    --ink: #23233a;
    --muted: #8a8ea8;
    --primary: #1f7ff0;
    --primary-soft: #dcebfd;
    --field-border: #cfe2fb;
    --toggle-track: #d6e7fc;
  }
  * { box-sizing: border-box; margin: 0; padding: 0; }
  html, body {
    width: 1200px;
    height: 2598px;
    overflow: hidden;
    background: var(--bg);
    font-family: "Poppins", sans-serif;
  }
  .screen {
    position: relative;
    width: 1200px;
    height: 2598px;
    background: var(--bg);
  }
  .back-button {
    position: absolute;
    left: 54px;
    top: 144px;
    width: 102px;
    height: 102px;
    border-radius: 50%;
    background: var(--primary-soft);
    display: flex;
    align-items: center;
    justify-content: center;
  }
  .page-title {
    position: absolute;
    left: 54px;
    top: 500px;
    font-size: 70px;
    font-weight: 700;
    color: var(--ink);
    letter-spacing: 0.5px;
  }
  .field {
    position: absolute;
    left: 102px;
    width: 995px;
    height: 154px;
    border: 3px solid var(--field-border);
    border-radius: 32px;
    display: flex;
    align-items: center;
    padding: 0 48px;
    font-size: 45px;
    color: var(--muted);
  }
  .field-username { top: 755px; }
  .field-email { top: 963px; }
  .field-password { top: 1171px; justify-content: space-between; }
  .terms-row {
    position: absolute;
    left: 102px;
    top: 1437px;
    width: 995px;
    height: 70px;
    display: flex;
    align-items: center;
    justify-content: space-between;
  }
  .terms-text {
    font-size: 44px;
    color: var(--muted);
  }
  .terms-link {
    color: var(--primary);
    font-weight: 600;
  }
  .toggle {
    position: relative;
    width: 128px;
    height: 70px;
    border-radius: 35px;
    background: var(--toggle-track);
  }
  .toggle-knob {
    position: absolute;
    right: 8px;
    top: 8px;
    width: 54px;
    height: 54px;
    border-radius: 50%;
    background: var(--primary);
  }
  .create-button {
    position: absolute;
    left: 198px;
    top: 2150px;
    width: 803px;
    height: 157px;
    border-radius: 26px;
    background: var(--primary);
    color: #fff;
    font-size: 45px;
    font-weight: 700;
    letter-spacing: 1.5px;
    display: flex;
    align-items: center;
    justify-content: center;
    box-shadow: 0 40px 50px -30px rgba(31, 127, 240, 0.45);
  }
  .login-prompt {
    position: absolute;
    left: 0;
    width: 1200px;
    top: 2455px;
    text-align: center;
    font-size: 44px;
    color: var(--muted);
  }
  .login-link {
    color: var(--ink);
    font-weight: 700;
  }
</style>
</head>
<body>
<main class="screen">
  <div class="back-button" aria-label="Back">
    <svg width="54" height="40" viewBox="0 0 54 40" fill="none">
      <path d="M50 20H6M20 5L5 20l15 15" stroke="#1f7ff0" stroke-width="6" stroke-linecap="round" stroke-linejoin="round"/>
    </svg>
  </div>

  <h1 class="page-title">Create an account</h1>

  <div class="field field-username">Username</div>
  <div class="field field-email">Email</div>
  <div class="field field-password">
    <span>Password</span>
    <svg width="52" height="38" viewBox="0 0 52 38" fill="none" aria-label="Show password">
      <path d="M3 19C9 8 17 3 26 3s17 5 23 16c-6 11-14 16-23 16S9 30 3 19z" stroke="#1f7ff0" stroke-width="5" stroke-linejoin="round"/>
      <circle cx="26" cy="19" r="7" fill="#1f7ff0"/>
    </svg>
  </div>

  <div class="terms-row">
    <p class="terms-text">I agree with all <span class="terms-link">Terms &amp;&nbsp; Conditions</span></p>
    <div class="toggle" aria-label="Agree toggle, on"><span class="toggle-knob"></span></div>
  </div>

  <div class="create-button">CREATE ACCOUNT</div>

  <p class="login-prompt">Already have an account? <span class="login-link">Log in</span></p>
</main>
</body>
</html>
```